Meridian Rest Supply Needs Business Card

Looking for a very nice looking business card. Creative but not extravagant. We sell beds and pillows across the U.S. and need something professional but catchy. I have attached the logo.

Name : Dale Fenwick
Title : President
Phone : (800) 417-2964
Email: sleep@quorvana.com
Website: www.quorvana.com

Can be single-sided or double-sided
horizontal or vertical

Can use Blues/Greys

Target Market(s)

Mass Market

Industry/Entity Type

Retail

Contact Information for Business Card

Name : Dale Fenwick
Title : President
Phone : (800) 417-2964
Email: sleep@quorvana.com
Website: www.quorvana.com

Requirements
Must have
• Clean, Modern, Smooth
• Can use Blues/Greys
• On the other side without the information - have something simple like www.quorvana.com or our logo
Nice to have
• Surprise me
Should not have
• Nothing crazy, nothing cluttered

```html
<!DOCTYPE html>
<html lang="en">
<head>
<meta charset="utf-8">
<title>Meridian Rest Supply – Business Card</title>
<link rel="stylesheet" href="https://fonts.googleapis.com/css2?family=Roboto:wght@300;400;700&display=swap">
<style>
  :root {
    --sky: #3ba7df;
    --sky-deep: #2f98d2;
    --slate: #7d7f82;
    --paper: #ffffff;
    --backdrop: #e9ecef;
    --ink-light: #ffffff;
  }
  html, body {
    margin: 0;
    width: 1200px;
    height: 950px;
    overflow: hidden;
    background: var(--backdrop);
    font-family: "Roboto", Arial, sans-serif;
  }
  .sheet {
    position: relative;
    width: 1200px;
    height: 950px;
  }
  .card {
    position: absolute;
    left: 250px;
    width: 700px;
    height: 400px;
    border-radius: 28px;
    overflow: hidden;
    box-shadow: 0 10px 28px rgba(0,0,0,0.18);
  }
  .card--front { top: 50px; background: var(--paper); }
  .card--back  { top: 500px; background: var(--sky); }

  .front-bands { position: absolute; inset: 0; }

  .brand-name {
    position: absolute;
    left: 0; right: 0;
    top: 105px;
    text-align: center;
    font-weight: 300;
    font-size: 92px;
    letter-spacing: 2px;
    color: var(--sky);
    line-height: 1;
  }
  .person {
    position: absolute;
    left: 34px;
    top: 318px;
    color: var(--ink-light);
    font-size: 21px;
    line-height: 1;
  }
  .person__name { font-weight: 700; }
  .person__title { font-weight: 300; }

  .contact {
    position: absolute;
    right: 34px;
    top: 282px;
    margin: 0;
    padding: 0;
    list-style: none;
    color: var(--ink-light);
    font-size: 17px;
    font-weight: 300;
    text-align: right;
  }
  .contact li {
    display: flex;
    align-items: center;
    justify-content: flex-end;
    gap: 10px;
    height: 24px;
  }
  .contact svg { width: 14px; height: 14px; flex: none; }

  .back-field {
    position: absolute;
    inset: 0;
    background: linear-gradient(135deg, var(--sky) 0%, var(--sky-deep) 100%);
  }
  .back-mark {
    position: absolute;
    left: 0; right: 0;
    top: 150px;
    display: flex;
    align-items: baseline;
    justify-content: center;
    gap: 10px;
    color: var(--ink-light);
    font-weight: 300;
  }
  .back-mark__prefix { font-size: 22px; letter-spacing: 6px; }
  .back-mark__name { font-size: 96px; letter-spacing: 2px; line-height: 1; }
  .back-mark__suffix { font-size: 20px; letter-spacing: 2px; }
</style>
</head>
<body>
<main class="sheet">

  <section class="card card--front" aria-label="Business card front">
    <svg class="front-bands" viewBox="0 0 700 400" aria-hidden="true">
      <path fill="var(--slate)"
            d="M0 290 H330 Q345 290 345 275 V256 Q345 242 360 242 H700 V400 H0 Z"/>
      <path fill="var(--sky)"
            d="M0 355 H355 Q370 355 370 340 V276 Q370 262 385 262 H700 V400 H0 Z"/>
    </svg>

    <div class="brand-name">quorvana</div>

    <p class="person">
      <span class="person__name">Dale Fenwick</span>
      <span class="person__title"> - President</span>
    </p>

    <ul class="contact">
      <li>(800) 417-2964
        <svg viewBox="0 0 24 24"><path fill="#fff" d="M6.6 10.8a15 15 0 0 0 6.6 6.6l2.2-2.2c.3-.3.7-.4 1-.2 1.1.4 2.3.6 3.6.6.6 0 1 .4 1 1V20c0 .6-.4 1-1 1A17 17 0 0 1 3 4c0-.6.4-1 1-1h3.5c.6 0 1 .4 1 1 0 1.3.2 2.5.6 3.6.1.3 0 .7-.2 1Z"/></svg>
      </li>
      <li>sleep@quorvana.com
        <svg viewBox="0 0 24 24"><rect x="2" y="5" width="20" height="14" rx="2" fill="#fff"/><path d="M3 6l9 7 9-7" stroke="var(--sky)" stroke-width="2" fill="none"/></svg>
      </li>
      <li>www.quorvana.com
        <svg viewBox="0 0 24 24"><circle cx="12" cy="12" r="10" fill="#fff"/><path d="M2 12h20M12 2c3 3 3 17 0 20M12 2c-3 3-3 17 0 20" stroke="var(--sky)" stroke-width="1.6" fill="none"/></svg>
      </li>
    </ul>
  </section>

  <section class="card card--back" aria-label="Business card back">
    <div class="back-field" role="img" aria-label="Faint repeating brand-name pattern across the blue background"></div>
    <div class="back-mark">
      <span class="back-mark__prefix">www.</span>
      <span class="back-mark__name">quorvana</span>
      <span class="back-mark__suffix">.com</span>
    </div>
  </section>

</main>
</body>
</html>
```